Real Estate Agent need a business card

I am a real estate agent in Vancouver, BC Canada. I recently used Brindlepane to develop a logo of my own. I would like to have my logo in the business card, as well my realty office logo also must be displayed along with its address. I also would like to have my headshot photo displayed in the business card on both sides.

Real Estate Agent

My office address:
Marwick Crest Realty
2218 Quillan St.
Vancouver, BC V7K 2P9

My contact information:
Cell: 604-555-0142
Office: 604-555-0187
Fax: 604-555-0188

My website : www.peterolsen.example
My email: email@peterolsen.example

My slogan: Simply I do. Far and Above.

• Front side(all in colour): My photo, My own logo, My office logo, My cell number, My website address and email, My slogan.
• Back side(could be black & white/ plz refer to the file name "preview"): My photo, My own logo, my office logo, my office address, my contact information.
• * Please read this: Since my logo has my name in it, there is no need to put my name in the card separately. As well, my office logo MUST BE displayed on both sides(you can reduce the size of office logo). But the office address can be displayed only one side, front or back. I would prefer to have my cell number only to be displayed prominently on the front side. So all the numbers should be displayed on the backside instead. Remember that I am trying to promote myself so the most important thing I consider from the front side of the card is my cell number, my website, and my email, not the office. The only thing I require by industry regulation from the front side is my office logo. Hope this helps.
• Colour on the front side and the black and white on the back side

```html
<!DOCTYPE html>
<html lang="en">
<head>
<meta charset="utf-8">
<title>Peter Olsen — Business Card</title>
<link rel="stylesheet" href="https://fonts.googleapis.com/css2?family=Montserrat:wght@500;700;800&family=Roboto+Condensed:wght@400;700&display=swap">
<style>
  :root {
    --bg: #c9ab82;
    --card-white: #f6f6f5;
    --ink: #2f3033;
    --charcoal: #3b3c3e;
    --olive: #4c5d3f;
    --lime: #7ab929;
    --pale: #e7e7e7;
    --muted: #b9bcb5;
    --photo-top: #9ea39a;
    --photo-bottom: #6f746c;
  }
  * { box-sizing: border-box; margin: 0; padding: 0; }
  html, body { width: 1200px; height: 969px; overflow: hidden; }
  body {
    background: var(--bg);
    font-family: "Montserrat", sans-serif;
    position: relative;
  }
  .card {
    position: absolute;
    top: 336px;
    width: 525px;
    height: 300px;
    background: var(--card-white);
    box-shadow: 0 14px 30px rgba(60, 40, 20, 0.35);
    overflow: hidden;
  }
  .card--front { left: 55px; }
  .card--back { left: 620px; display: flex; }

  /* personal brand lockup */
  .brand { display: flex; flex-direction: column; align-items: flex-start; }
  .brand__row { display: flex; align-items: center; gap: 10px; }
  .brand__mark { width: 26px; height: 26px; background: var(--lime); flex: none; }
  .brand__name {
    font-weight: 800;
    color: var(--ink);
    font-size: 27px;
    letter-spacing: 0.5px;
    line-height: 1;
    white-space: nowrap;
  }
  .brand__role {
    font-weight: 700;
    color: var(--lime);
    font-size: 10px;
    letter-spacing: 3px;
    margin: 6px 0 0 36px;
    white-space: nowrap;
  }

  /* headshot placeholder */
  .headshot {
    background: linear-gradient(180deg, var(--photo-top), var(--photo-bottom));
  }

  /* office mark */
  .office {
    display: flex;
    align-items: center;
    gap: 6px;
    font-family: "Montserrat", sans-serif;
    font-weight: 700;
    font-size: 9px;
    letter-spacing: 1.2px;
    color: var(--ink);
    white-space: nowrap;
  }
  .office__mark { width: 10px; height: 10px; background: var(--ink); flex: none; }

  /* front */
  .front__brand { position: absolute; left: 40px; top: 62px; }
  .front__slogan {
    position: absolute;
    left: 40px;
    top: 130px;
    font-weight: 500;
    font-size: 12px;
    color: var(--ink);
    letter-spacing: 0.4px;
  }
  .front__headshot {
    position: absolute;
    right: 40px;
    top: 36px;
    width: 120px;
    height: 148px;
  }
  .front__contact {
    position: absolute;
    left: 0;
    right: 0;
    bottom: 0;
    height: 82px;
    background: var(--charcoal);
    color: var(--pale);
    font-family: "Roboto Condensed", sans-serif;
    display: flex;
    align-items: center;
    padding: 0 40px;
    gap: 24px;
  }
  .front__cell {
    font-family: "Montserrat", sans-serif;
    font-weight: 800;
    font-size: 22px;
    color: #fff;
    line-height: 1.1;
    white-space: nowrap;
  }
  .front__cell small {
    display: block;
    font-family: "Roboto Condensed", sans-serif;
    font-weight: 700;
    font-size: 10px;
    letter-spacing: 2.5px;
    color: var(--lime);
  }
  .front__online {
    list-style: none;
    font-size: 12px;
    line-height: 1.6;
    color: var(--muted);
    border-left: 2px solid var(--olive);
    padding-left: 16px;
  }
  .front__office {
    position: absolute;
    right: 40px;
    top: 194px;
  }

  /* back */
  .back__logo-side {
    width: 46%;
    display: flex;
    flex-direction: column;
    align-items: center;
    justify-content: center;
    gap: 14px;
  }
  .back__headshot { width: 66px; height: 80px; }
  .back__logo-side .brand__name { font-size: 20px; }
  .back__logo-side .brand__mark { width: 20px; height: 20px; }
  .back__logo-side .brand__role { font-size: 7.5px; letter-spacing: 2.2px; margin-left: 30px; }

  .back__info {
    width: 54%;
    background: var(--charcoal);
    display: flex;
    flex-direction: column;
    font-family: "Roboto Condensed", sans-serif;
    color: var(--pale);
  }
  .address {
    font-style: normal;
    padding: 20px 24px 0;
    height: 95px;
    font-size: 13px;
    line-height: 1.45;
    letter-spacing: 0.4px;
  }
  .address strong { font-weight: 700; color: #fff; }
  .identity {
    background: var(--olive);
    padding: 16px 24px;
    height: 78px;
  }
  .identity__name {
    font-family: "Montserrat", sans-serif;
    font-weight: 800;
    font-size: 24px;
    color: #fff;
    letter-spacing: 0.5px;
  }
  .identity__title {
    font-size: 11.5px;
    letter-spacing: 2.5px;
    text-transform: uppercase;
    color: var(--pale);
    margin-top: 2px;
  }
  .contacts {
    list-style: none;
    padding: 14px 24px 0;
    font-size: 11px;
    line-height: 1.55;
    color: var(--muted);
  }
  .contacts li { display: flex; align-items: center; gap: 8px; white-space: nowrap; }
  .contacts svg { width: 10px; height: 10px; flex: none; }
</style>
</head>
<body>
  <section class="card card--front" aria-label="Business card front">
    <div class="brand front__brand">
      <div class="brand__row">
        <span class="brand__mark"></span>
        <span class="brand__name">PETER OLSEN</span>
      </div>
      <span class="brand__role">REAL ESTATE AGENT</span>
    </div>
    <p class="front__slogan">Simply I do. Far and Above.</p>
    <div class="headshot front__headshot" role="img" aria-label="Headshot photo of the agent"></div>
    <div class="office front__office"><span class="office__mark"></span>MARWICK CREST REALTY</div>
    <div class="front__contact">
      <div class="front__cell"><small>CELL</small>604-555-0142</div>
      <ul class="front__online">
        <li>www.peterolsen.example</li>
        <li>email@peterolsen.example</li>
      </ul>
    </div>
  </section>

  <section class="card card--back" aria-label="Business card back">
    <div class="back__logo-side">
      <div class="headshot back__headshot" role="img" aria-label="Headshot photo of the agent"></div>
      <div class="brand">
        <div class="brand__row">
          <span class="brand__mark"></span>
          <span class="brand__name">PETER OLSEN</span>
        </div>
        <span class="brand__role">REAL ESTATE AGENT</span>
      </div>
      <div class="office"><span class="office__mark"></span>MARWICK CREST REALTY</div>
    </div>
    <div class="back__info">
      <address class="address">
        <strong>Marwick Crest Realty</strong><br>
        2218 Quillan St.<br>
        Vancouver, BC V7K 2P9
      </address>
      <div class="identity">
        <div class="identity__name">ALEX MORGAN</div>
        <div class="identity__title">General Manager</div>
      </div>
      <ul class="contacts">
        <li>
          <svg viewBox="0 0 10 10"><path d="M2 1 L4 1 L4.6 3 L3.5 4 Q4.5 6 6 6.5 L7 5.4 L9 6 L9 8 Q5 9 2 6 Q0.5 3.5 2 1Z" fill="currentColor"/></svg>
          Cell 604-555-0142
        </li>
        <li>
          <svg viewBox="0 0 10 10"><path d="M2 1 L4 1 L4.6 3 L3.5 4 Q4.5 6 6 6.5 L7 5.4 L9 6 L9 8 Q5 9 2 6 Q0.5 3.5 2 1Z" fill="currentColor"/></svg>
          Office 604-555-0187
        </li>
        <li>
          <svg viewBox="0 0 10 10"><rect x="1.5" y="1" width="7" height="8" fill="none" stroke="currentColor"/><line x1="3" y1="4" x2="7" y2="4" stroke="currentColor"/><line x1="3" y1="6" x2="7" y2="6" stroke="currentColor"/></svg>
          Fax 604-555-0188
        </li>
        <li>
          <svg viewBox="0 0 10 10"><rect x="0.5" y="2" width="9" height="6" fill="none" stroke="currentColor"/><path d="M0.5 2 L5 5.5 L9.5 2" fill="none" stroke="currentColor"/></svg>
          email@peterolsen.example
        </li>
        <li>
          <svg viewBox="0 0 10 10"><circle cx="5" cy="5" r="4.2" fill="none" stroke="currentColor"/><ellipse cx="5" cy="5" rx="1.8" ry="4.2" fill="none" stroke="currentColor"/><line x1="0.8" y1="5" x2="9.2" y2="5" stroke="currentColor"/></svg>
          www.peterolsen.example
        </li>
      </ul>
    </div>
  </section>
</body>
</html>
```